Sedona Themed Wedding Invitation & RSVP

*We have added our "Save the Date" for reference. We are not looking for an exact match, but we'd like the invitation and the "Save the Date" to coordinate. Our wedding colors are light pink, light green, cream, and gold. We have also added pictures of bouquets to give you an idea of the color palette and also examples of flowers and greenery to use in the invitation. What we like about the "Save the Date" is that it draws on the wedding colors and brings them in through the colors of the sunset.
*We have also added additional pictures the venue, the Le Verger Lodge, and several maps. We hope that you can use these to get a better feel for our venue and the theme of our wedding. It will be soft and romantic and at the very height of spring.
* We appreciated that many designers incorporated the Lodge at Le Vergre, we'd like to see more of that.
*Please note that we included some photos of Sedona for inspiration, please do not feel tied to these, do your own research and find what works best with your design.
*These maps are being included as references, but they are the work of other artists. Please make your own map from scratch and use these as references.
We would like a vertical quad-fold wedding invitation that has a perforated edge RSVP which can be sent as a postcard.
We have attached pictures of a similar style of invitation to serve as an example of the overall style we are looking for. We would like to see the end project be in a similar style of watercolor, but it would be Sedona themed throughout (rather than the forest theme presented in the attached example). We have also attached pictures of Sedona to serve as further inspiration. Below, we have provided an outline organized by panel (four panels on the front and four panels on the back) with descriptions of the more specific details:
-Front four panels:
-Panel 1: "Please join us for the wedding of Tobias and Colette"
-Panel 2: "Come out and celebrate. [INSERT TIME OF WEDDING HERE]
Saturday, May First 2021 at Le Verger de Rimoux"
-Panel 3: Custom map of Sedona. Include Le Verger de Rimoux on the
map (exemplar picture is of an idea for this is also included below)
- Panel 4: RSVP similar to one in the exemplar invitation. For RSVP date
deadline use April 1st, 2021. Address is 2287 W Marlow St Phoenix, AZ
85019
-Back four panels:
-Panel 1: Venue: Le Verger de Rimoux. 418 Fennick Ln, Sedona, AZ 86339.
Please arrive no earlier than XXX PM when valet services begin. Dinner
and dancing to follow the ceremony
-Panel 2: Hotels: Le Verger de Rimoux 418 Fennick Ln, Sedona, AZ 86339
(800) 612-3908; Bramwell Inn 917 N Tolliver Rd, Sedona, AZ 86339
(855) 238-6041.
"Hotel reservations can also be made through the links provided on our
website"
- Panel 3: "We have reserved a block of rooms for our guests. Please
mention the Pruett Halloway Wedding when you call to reserve."
"For additional details, please visit our wedding website and take a walk
down memory lane with us as we prepare to celebrate the rest of our
lives together: [INSERT WEDDING WEBSITE HERE AND
PASSWORD]"
- Panel 4: "Ceremony and celebration will be outdoors. Semi-formal attire
and flat shoes are recommended."
"Additionally, although we love your children, we want our wedding to
be your night off! Please know space is very limited; accordingly, we
encourage a weekend getaway for the grownups."
We'd like to have a succulent and rose at the bottom of the panel (an
exemplar picture is of an idea for this is also included below)
Updates
We have given extensive feedback to designers and would like to give them time to adjust their designs. Additionally, we have incorporated a lot more images into the brief that we hope will help!

```html
<!DOCTYPE html>
<html lang="en">
<head>
<meta charset="utf-8">
<title>Tobias &amp; Colette — Quad-fold Wedding Invitation</title>
<link rel="stylesheet" href="https://fonts.googleapis.com/css2?family=Archivo+Black&family=Dancing+Script:wght@500;700&family=Pathway+Gothic+One&display=swap">
<style>
:root{
  --ink:#000000;
  --brown:#5b4526;
  --red:#e3322a;
  --paper:#f1eadb;
  --paper-edge:#e5c49a;
  --sky:#9fc1dc;
  --rock:#d4502a;
  --brush:#3d7a35;
  --map-green:#a9e4b9;
  --map-light:#d3f3da;
  --rose:#ec8fb0;
  --succulent:#a6dd9a;
  --caps:"Pathway Gothic One",sans-serif;
  --script:"Dancing Script",cursive;
  --hand:"Dancing Script",cursive;
  --slab:"Archivo Black",sans-serif;
}
*{margin:0;padding:0;box-sizing:border-box}
html,body{width:960px;height:1200px;overflow:hidden;background:#fff}
.canvas{position:relative;width:960px;height:1200px}
.side-label{position:absolute;left:0;right:0;text-align:center;font-family:var(--slab);font-size:48px;font-weight:400;color:var(--ink);line-height:1}
.side-label.front{top:80px}
.side-label.back{top:618px}
.spread{position:absolute;left:32px;width:896px;height:392px;display:flex}
.spread.front{top:166px}
.spread.back{top:724px}
.panel{position:relative;width:224px;height:392px;overflow:hidden;
  background:radial-gradient(ellipse at center,var(--paper) 55%,var(--paper-edge) 130%);color:var(--brown)}
.row{position:absolute;left:0;right:0;text-align:center;line-height:1.15}
.caps{font-family:var(--caps);letter-spacing:.5px;text-transform:uppercase}
.script{font-family:var(--script);font-weight:700}
.hand{font-family:var(--hand);font-weight:500}
.red{color:var(--red)}
.rule{position:absolute;left:26px;right:26px;height:1px;background:var(--brown);opacity:.7}

/* front panel 1 */
.cover{background:linear-gradient(180deg,var(--sky) 0%,#c3d7e4 28%,var(--rock) 40%,#c2461f 52%,var(--brush) 66%,#2f5e2a 84%,#6b6058 100%)}
.cover .caps{color:var(--brown)}
.cover .names{color:#fff;font-family:var(--script);font-weight:700;text-shadow:0 1px 2px rgba(0,0,0,.35)}
.ribbon{position:absolute;left:50%;transform:translateX(-50%);height:18px;width:60px;background:var(--brown);color:var(--paper);font-family:var(--caps);font-size:12px;line-height:18px;text-align:center}

/* map panel */
.map{background:linear-gradient(160deg,var(--map-light) 0%,var(--map-green) 45%,#bfeccb 75%,var(--map-light) 100%)}

/* RSVP */
.choice{position:absolute;left:34px;font-size:10px;display:flex;align-items:center;gap:4px;white-space:nowrap}
.choice .dot{width:9px;height:9px;border:1px solid var(--brown);border-radius:50%}
.choice b{font-family:var(--script);font-weight:700;font-size:14px;color:var(--red)}
.choice span{font-family:var(--hand)}

/* bouquet area */
.flowers{position:absolute;left:37px;width:150px;height:96px;top:236px;border-radius:48px;
  background:radial-gradient(ellipse at 50% 50%,var(--succulent) 0%,var(--rose) 55%,rgba(236,143,176,0) 100%)}
</style>
</head>
<body>
<main class="canvas">
  <h2 class="side-label front">Front</h2>

  <section class="spread front">
    <article class="panel cover">
      <div role="img" aria-label="Photograph of Sedona red rock buttes above a green, rocky creek" style="position:absolute;inset:0"></div>
      <p class="row caps" style="top:38px;font-size:11px;letter-spacing:2px"><span class="red">&larr;</span> Please join us <span class="red">&rarr;</span></p>
      <p class="row hand" style="top:50px;font-size:15px;color:var(--brown)">for the</p>
      <p class="row caps red" style="top:70px;font-size:32px;letter-spacing:1px">&middot;Wedding&middot;</p>
      <div class="ribbon" style="top:114px">OF</div>
      <p class="row names" style="top:180px;font-size:46px">Tobias</p>
      <p class="row names" style="top:228px;font-size:26px">and</p>
      <p class="row names" style="top:256px;font-size:46px">Colette</p>
    </article>

    <article class="panel date">
      <p class="row caps" style="top:58px;font-size:15px">&bull; Come out and celebrate &bull;</p>
      <p class="row script" style="top:84px;font-size:68px">May</p>
      <p class="row caps" style="top:174px;font-size:30px;letter-spacing:2px">First&nbsp;&nbsp;2021</p>
      <p class="row caps" style="top:204px;font-size:19px">Saturday <span class="red">|</span> <span style="font-size:8px;display:inline-block;width:46px;line-height:1;text-align:left">[Insert time of wedding here]</span></p>
      <div class="ribbon" style="top:248px">AT</div>
      <p class="row script" style="top:282px;font-size:24px">Le Verger</p>
      <p class="row script" style="top:306px;font-size:24px">de Rimoux</p>
    </article>

    <article class="panel map" role="img" aria-label="Watercolour map of Sedona marking the venue, hotels, bridges, rock formations and the creek"></article>

    <article class="panel rsvp">
      <p class="row caps" style="top:38px;font-size:11px;letter-spacing:2px"><span class="red">&larr;</span> Please respond by <span class="red">&rarr;</span></p>
      <p class="row caps" style="top:60px;font-size:22px">
        <span style="position:relative;top:-8px">April</span>
        <span style="font-family:var(--slab);font-size:42px;margin:0 6px;text-transform:none">1st</span>
        <span style="position:relative;top:-8px">2021</span>
      </p>
      <p class="script" style="position:absolute;left:34px;top:116px;font-size:20px">M</p>
      <div class="rule" style="top:136px;left:46px"></div>
      <div class="choice" style="top:166px"><i class="dot"></i><b>Yes!</b><span>I'm ready to attack the dance floor</span></div>
      <div class="choice" style="top:183px"><i class="dot"></i><b>No!</b><span>I will forever regret this decision</span></div>
      <p class="row script red" style="top:212px;font-size:12px">Favorite Song...</p>
      <div class="rule" style="top:236px"></div>
      <p class="row script" style="top:256px;font-size:54px">T<span style="font-size:24px">&amp;</span>C</p>
      <p class="row caps" style="top:324px;font-size:16px">2287 W Marlow St Phoenix,<br>AZ 85019</p>
    </article>
  </section>

  <h2 class="side-label back">Back</h2>

  <section class="spread back">
    <article class="panel venue">
      <p class="row script red" style="top:66px;font-size:52px">Venue</p>
      <p class="row script" style="top:152px;font-size:27px">Le Verger</p>
      <p class="row script" style="top:178px;font-size:27px">de Rimoux</p>
      <div class="rule" style="top:232px"></div>
      <p class="row caps" style="top:236px;font-size:19px">418 Fennick Ln, Sedona,<br>AZ 86339</p>
      <div class="rule" style="top:281px"></div>
      <p class="row" style="top:302px;font-family:var(--caps);font-size:10px;line-height:1.25">Please arrive no earlier than XXX PM<br>when valet services begin.<br>Dinner and dancing to follow the ceremony.</p>
    </article>

    <article class="panel hotel">
      <p class="row script red" style="top:62px;font-size:52px">Hotel</p>
      <p class="row script" style="top:152px;font-size:27px">Le Verger</p>
      <p class="row script" style="top:178px;font-size:27px">de Rimoux</p>
      <div class="rule" style="top:224px"></div>
      <p class="row caps" style="top:226px;font-size:16px">418 Fennick Ln, Sedona, AZ 86339</p>
      <p class="row" style="top:250px;font-family:var(--caps);font-size:11px">Bramwell Inn 917 N Tolliver Rd, Sedona,<br>AZ 86339</p>
      <p class="row caps red" style="top:290px;font-size:15px">(800) 612-3908 <span style="color:var(--brown)">|</span> (855) 238-6041</p>
      <p class="row" style="top:314px;font-family:var(--caps);font-size:11px">"Hotel reservations can also be made<br>through the links provided on our website"</p>
    </article>

    <article class="panel block">
      <p class="row caps" style="top:70px;font-size:16px">We have reserved a block<br>of rooms for our guests</p>
      <p class="row script red" style="top:124px;font-size:18px">&bull; Please Mention &bull;</p>
      <p class="row caps" style="top:150px;font-size:15px">The Pruett Halloway Wedding<br>when you call to reserve.</p>
      <p class="row hand" style="top:200px;font-size:12px;line-height:1.25">For additional details,<br>please visit our wedding website<br>and take a walk down memory lane<br>with us as we prepare to celebrate<br>the rest of our lives together.</p>
      <p class="row caps red" style="top:294px;font-size:12px">[Insert wedding website<br>and password here]</p>
    </article>

    <article class="panel notes">
      <p class="row" style="top:58px;font-family:var(--caps);font-size:11px;line-height:1.3">Ceremony and celebration will be outdoors.<br>Semi formal attire and flat shoes are recommended.</p>
      <p class="row hand" style="top:102px;font-size:12px;line-height:1.33">Additionally,<br>although we love your children,<br>we want our wedding to be your night off!<br>Please know space is very limited;<br>accordingly,<br>we encourage a weekend getaway<br>for the grownups.</p>
      <div class="flowers" role="img" aria-label="Watercolour cluster of pink roses around a pale green succulent with dark leaves"></div>
    </article>
  </section>
</main>
</body>
</html>
```